Property development & Investment company Need a logo & business card design

Our name is KT Estates Australia Pty Ltd
Need logo & business card design

Target Market(s)

People dealing in commercial property

Industry/Entity Type

Business

Contact Information for Business Card

KT Estates Australia
Peter Dunmore Mobile0419 703 646
Email Peter@quillbarrow.com.au

Font styles to use
Sans Serif

Requirements
Must have
• company name
• contact details
Nice to have
• KT Estates Bold
• Australia Not Bold
Should not have
• To busy of a look

```html
<!DOCTYPE html>
<html lang="en">
<head>
<meta charset="utf-8">
<title>KT Estates Australia – Business Card</title>
<link href="https://fonts.googleapis.com/css2?family=Lato:wght@400;700&display=swap" rel="stylesheet">
<style>
  :root {
    --brand-blue: #2156a0;
    --card-white: #ffffff;
    --divider-grey: #9a9a9a;
    --stage-bg: #e6e8ec;
    --text-light: #ffffff;
  }
  * { box-sizing: border-box; margin: 0; padding: 0; }
  html, body {
    width: 1200px;
    height: 900px;
    overflow: hidden;
    background: var(--stage-bg);
    font-family: "Lato", sans-serif;
  }
  .canvas {
    position: relative;
    width: 1200px;
    height: 900px;
  }
  .card {
    position: absolute;
    left: 260px;
    width: 680px;
    height: 390px;
    box-shadow: 0 6px 18px rgba(0,0,0,0.18);
    overflow: hidden;
  }
  .card-front {
    top: 40px;
    background: var(--brand-blue);
    display: flex;
    align-items: center;
    justify-content: center;
  }
  .card-back {
    top: 470px;
    display: flex;
  }
  .wordmark {
    display: flex;
    align-items: center;
    gap: 14px;
    font-weight: 700;
    white-space: nowrap;
  }
  .wordmark-dot {
    width: 18px;
    height: 18px;
    border-radius: 50%;
    flex: none;
  }
  .card-front .wordmark { color: var(--text-light); font-size: 50px; letter-spacing: -0.5px; }
  .card-front .wordmark-dot { background: var(--text-light); }
  .back-brand {
    width: 290px;
    background: var(--card-white);
    border-right: 4px solid var(--divider-grey);
    display: flex;
    align-items: center;
    justify-content: center;
  }
  .back-brand .wordmark { color: var(--brand-blue); font-size: 25px; gap: 8px; }
  .back-brand .wordmark-dot { background: var(--brand-blue); width: 10px; height: 10px; }
  .back-contact {
    flex: 1;
    background: var(--brand-blue);
    color: var(--text-light);
    padding: 130px 0 0 70px;
  }
  .contact-name { font-size: 30px; font-weight: 400; line-height: 1.1; }
  .contact-role { font-size: 19px; margin-top: 4px; }
  .contact-list { list-style: none; margin-top: 22px; }
  .contact-item {
    display: flex;
    align-items: center;
    gap: 12px;
    font-size: 21px;
    line-height: 1.4;
  }
  .contact-icon { width: 18px; height: 18px; flex: none; }
</style>
</head>
<body>
  <main class="canvas">
    <section class="card card-front" aria-label="Card front">
      <div class="wordmark">
        <span class="wordmark-dot"></span>
        <span class="wordmark-name">KT Estates Australia</span>
      </div>
    </section>

    <section class="card card-back" aria-label="Card back">
      <div class="back-brand">
        <div class="wordmark">
          <span class="wordmark-dot"></span>
          <span class="wordmark-name">KT Estates Australia</span>
        </div>
      </div>
      <div class="back-contact">
        <h1 class="contact-name">Peter Dunmore</h1>
        <p class="contact-role">Manager</p>
        <ul class="contact-list">
          <li class="contact-item">
            <svg class="contact-icon" viewBox="0 0 18 18" aria-hidden="true">
              <rect x="5" y="1" width="8" height="16" rx="1.5" fill="none" stroke="#fff" stroke-width="1.6"/>
              <line x1="7" y1="14" x2="11" y2="14" stroke="#fff" stroke-width="1.4"/>
            </svg>
            <span>0438 512 907</span>
          </li>
          <li class="contact-item">
            <svg class="contact-icon" viewBox="0 0 18 18" aria-hidden="true">
              <rect x="1" y="4" width="16" height="11" fill="#fff"/>
              <polyline points="1,4 9,10.5 17,4" fill="none" stroke="#2156a0" stroke-width="1.4"/>
            </svg>
            <span>Peter@quillbarrow.com.au</span>
          </li>
        </ul>
      </div>
    </section>
  </main>
</body>
</html>
```